Web Site for Strategy and Technology Consulting Company

We are looking for a website design that engages potential customers to understand our services and contact us. In this contest, we are looking for a homepage design, but the winning designer will be favored for the design of some of the more complicated interior pages of the site. An additional contest (or contests) for these pages will be added soon.

PLATROM AND RESPONSIVE DESIGN
The site will be implemented in WordPress using the Elementor page builder.
We are looking for a design that will look good on phones are well as laptop browsers.

UPLOADED FILES INCLUDE:
1a A wireframe of the homepage we are looking for. The Uploaded PDF also includes a draft of the text proposed for the homepage. Designers are free to go beyond the wireframe, but all elements of the wireframe should be included.
1b A Word document with the draft text of the homepage.
2a-d The Norvalith logo. Two versions are included – a dark version which works well against a light background, and a light version which works well against a dark background.
3 The Norvalith color palette with HEX and RGB values. Designers are not limited to this palette, but colors should be complementary.
4 A draft of the homepage menu
5 Service sheets with information on the services we provide

MORE ABOUT NORVALITH
Norvalith is a consulting company focused on transforming businesses through software. Our tagline, “Transformation Delivered,” recognizes the gap business often have between business transformation and the software they end up with. By listening to our customers and understanding their vision and where they are, we help get our customers where they want to go.

We increase our capability by working with many consultants and partners, allowing us to provide our customers with the best people and the software that best suits them.

Industry/Entity Type

Consulting

Number of Pages Required

1 page

Font styles to use
Sans Serif

Requirements
Must have
• the content represented on the wireframe uploaded
Nice to have
• interactive features, such as roll-over icons that reveal additional information

```html
<!DOCTYPE html>
<html lang="en">
<head>
<meta charset="utf-8">
<title>Norvalith — Transformation Delivered</title>
<link href="https://fonts.googleapis.com/css2?family=Fira+Sans:ital,wght@0,300;0,400;0,500;0,600;1,400&display=swap" rel="stylesheet">
<style>
:root{
  --ink:#14171f;
  --muted:#4a4f5a;
  --soft:#8a8f98;
  --yellow:#f2c40f;
  --cta-bg:#f9e38a;
  --navy:#070d19;
  --deep-blue:#0c2c5e;
  --bright-blue:#1a6fd1;
  --card-blue:#d9e8f6;
  --icon-blue:#1f4e8c;
  --tint:#f4f6fc;
  --quote-bg:#e7edf8;
  --white:#ffffff;
}
*{box-sizing:border-box;margin:0;padding:0}
html,body{width:1200px;height:4164px;overflow:hidden;background:var(--white)}
body{font-family:"Fira Sans",sans-serif;color:var(--ink);position:relative}
.btn{display:inline-flex;align-items:center;justify-content:center;background:var(--yellow);color:var(--ink);border-radius:22px;font-size:18px;font-weight:500;text-decoration:none;height:42px}
.abs{position:absolute}

/* hero */
.hero{position:absolute;left:0;top:0;width:1200px;height:690px;
  background:radial-gradient(ellipse 520px 420px at 1050px 300px,#1b5fb0 0%,#0d3170 40%,rgba(7,13,25,0) 75%),
             radial-gradient(ellipse 300px 200px at 900px 650px,#0f3a7a 0%,rgba(7,13,25,0) 70%),var(--navy);
  color:var(--white)}
.site-header{position:absolute;left:0;top:0;width:1200px;height:100px;border-bottom:1px solid rgba(255,255,255,.25)}
.brand{position:absolute;left:128px;top:18px;display:flex;align-items:center;gap:10px;font-size:54px;font-weight:300;color:var(--white);letter-spacing:-.5px}
.brand .dot{width:12px;height:12px;border-radius:50%;background:var(--yellow)}
.nav{position:absolute;left:455px;top:40px;display:flex;gap:44px;font-size:17px;font-weight:500}
.nav span::after{content:"⌄";font-size:12px;margin-left:4px}
.header-cta{position:absolute;left:928px;top:30px;width:144px}
.hero h1{position:absolute;left:126px;top:188px;font-size:53px;font-weight:500;letter-spacing:-.3px}
.hero-lead{position:absolute;left:126px;top:264px;width:600px;font-size:16.5px;line-height:22px}
.hero-list{position:absolute;left:142px;top:378px;list-style:none;font-size:14.5px;line-height:25px}
.hero-list li::before{content:"";display:inline-block;width:10px;height:10px;background:var(--yellow);margin-right:8px}
.hero-tag{position:absolute;left:128px;top:498px;font-size:20px}
.hero .btn{position:absolute;left:128px;top:545px;width:143px}

/* technology */
.tech-head{position:absolute;left:0;top:783px;width:1200px;text-align:center}
.tech-head h2{font-size:43px;font-weight:500}
.tech-head p{width:840px;margin:18px auto 0;font-size:16.5px;line-height:25px;color:var(--muted)}
.tech-head .btn{margin-top:26px;width:168px;height:40px}
.service-cards{position:absolute;left:79px;top:1038px;display:flex;gap:17px}
.service-card{width:195px;height:248px;background:var(--card-blue);text-align:center;padding-top:28px}
.service-icon{width:76px;height:76px;margin:0 auto 14px;background:linear-gradient(135deg,#7fa6d2,#1f4e8c);border-radius:6px;opacity:.75}
.service-card h3{font-size:17px;font-weight:500;line-height:22px;height:46px;display:flex;align-items:center;justify-content:center}
.service-card p{font-size:13px;line-height:17px;color:var(--muted);margin:8px 22px 0}
.sub-brand{height:76px;margin-bottom:14px;display:flex;flex-direction:column;justify-content:center;color:var(--icon-blue)}
.sub-brand b{font-size:24px;font-weight:500}
.sub-brand small{font-size:11px;color:var(--soft)}
.tech-note{position:absolute;left:0;top:1330px;width:1200px;text-align:center;font-size:16.5px;color:var(--muted)}
.wave-band{position:absolute;left:0;top:1400px;width:1200px;height:310px;background:linear-gradient(180deg,rgba(220,224,232,0) 0%,rgba(220,224,232,.45) 50%,rgba(220,224,232,0) 100%)}

/* people */
.people h2{position:absolute;left:126px;top:1728px;font-size:43px;font-weight:500}
.people-copy{position:absolute;left:128px;top:1800px;width:490px;font-size:16.5px;line-height:25px;color:var(--muted)}
.people-copy ul{list-style:none;margin:14px 0}
.people-copy li{padding-left:22px;position:relative;margin-bottom:24px}
.people-copy li::before{content:"";position:absolute;left:0;top:8px;width:10px;height:10px;background:var(--yellow)}
.people .btn{position:absolute;left:128px;top:2143px;width:167px}
.people-photo{position:absolute;left:677px;top:1763px;width:401px;height:435px;background:linear-gradient(160deg,#dfe6ec 0%,#b9a58a 55%,#9a6e45 100%)}

/* testimonials */
.testimonials{position:absolute;left:0;top:2325px;width:1200px;height:680px;background:var(--tint)}
.testimonials h2{position:absolute;left:0;top:80px;width:1200px;text-align:center;font-size:43px;font-weight:500}
.t-item{position:absolute;left:127px;width:390px;height:90px;display:flex;align-items:center;gap:18px;padding-left:13px}
.t-item.active{background:var(--white);box-shadow:0 4px 14px rgba(30,40,70,.12)}
.avatar{width:64px;height:64px;background:linear-gradient(160deg,#cfd6de,#8e99a6)}
.t-item b{display:block;font-size:16.5px;font-weight:500}
.t-item span{font-size:15.5px;color:var(--soft)}
.quote-panel{position:absolute;left:575px;top:173px;width:497px;height:372px;background:var(--quote-bg);padding:50px 52px}
.quote-panel svg{display:block}
.quote-panel p{margin-top:14px;font-style:italic;font-size:17.5px;line-height:30px;color:var(--muted)}
.quote-panel b{display:block;margin-top:18px;margin-left:6px;font-size:19px;font-weight:500}

/* partners */
.partners h2{position:absolute;left:0;top:3112px;width:1200px;text-align:center;font-size:43px;font-weight:500}
.partners-sub{position:absolute;left:0;top:3176px;width:1200px;text-align:center;font-size:20px;color:var(--soft)}
.partner-row{position:absolute;left:150px;top:3252px;width:900px;height:70px;display:flex;justify-content:space-around;align-items:center}
.partner{display:flex;align-items:center;gap:10px;font-size:28px;font-weight:400;color:var(--icon-blue)}
.partner i{width:14px;height:14px;border-radius:50%;background:var(--icon-blue)}
.arrow{position:absolute;top:3262px}

/* cta */
.cta{position:absolute;left:130px;top:3418px;width:942px;height:327px;background:var(--cta-bg);text-align:center;padding-top:78px}
.cta p{font-size:30px;line-height:39px;width:640px;margin:0 auto;font-weight:400}
.cta .btn{margin-top:32px;width:168px;height:40px}

/* footer */
.site-footer .brand{top:3838px;color:var(--ink)}
.footer-about{position:absolute;left:127px;top:3930px;width:250px;font-size:14px;line-height:20px;color:var(--muted)}
.f-col{position:absolute;top:3848px;font-size:14.5px;line-height:23px;color:var(--muted)}
.f-col h4{font-size:15.5px;font-weight:500;color:var(--ink);display:inline-block;border-bottom:2px solid var(--ink);padding-bottom:3px;margin-bottom:6px}
.f-col a{display:block;color:inherit;text-decoration:none}
.contact-row{display:flex;gap:12px;margin-bottom:14px;line-height:18px}
.contact-row .ic{width:30px;height:30px;background:#1e64b8;display:flex;align-items:center;justify-content:center;flex:none}
.footer-rule{position:absolute;left:128px;top:4090px;width:944px;height:1px;background:#cfd3da}
.copyright{position:absolute;left:0;top:4122px;width:1200px;text-align:center;font-size:14.5px;color:var(--muted)}
</style>
</head>
<body>

<section class="hero">
  <header class="site-header">
    <div class="brand"><span class="dot"></span>Norvalith</div>
    <nav class="nav"><span>About Us</span><span>Services</span><span>Insights</span><span>Join Us</span></nav>
    <a class="btn header-cta">Contact Us</a>
  </header>
  <h1>Transformation Delivered.</h1>
  <p class="hero-lead">We do more for our customers than implement software. We listen. We work to understand where they are in their transformation journey and where they want to go. We partner with them to clear the roadblocks that stand in their way, ensuring they reach their destination. At Norvalith, we:</p>
  <ul class="hero-list">
    <li>Focus on business value, with an emphasis on delivering value quickly.</li>
    <li>Meet our customers where they are without backing them up to the beginning of their journey.</li>
    <li>Provide a wide range of services, from strategy to product support.</li>
    <li>Commit to our customer’s long-term success.</li>
  </ul>
  <p class="hero-tag">Norvalith is business transformation, delivered.</p>
  <a class="btn">Our Story</a>
</section>

<section class="technology">
  <div class="tech-head">
    <h2>Transformation Supported by Technology</h2>
    <p>During our early years, Norvalith focused only on business transformation. We came to realize that successful transformation often depended on quality software implementations, and often more than one. Now we focus on five things, the five things most businesses need to reach their goals.</p>
    <a class="btn">How We Work</a>
  </div>
  <div class="service-cards">
    <article class="service-card"><div class="service-icon" role="img" aria-label="Strategy dashboard icon"></div><h3>Business<br>Transformation</h3><p>Define and execute your strategy.</p></article>
    <article class="service-card"><div class="service-icon" role="img" aria-label="ERP gear icon"></div><h3>ERP<br>Implementations</h3><p>Assess, upgrade, and implement ERP solutions to meet your needs.</p></article>
    <article class="service-card"><div class="service-icon" role="img" aria-label="CRM relationships icon"></div><h3>CRM<br>Implementations</h3><p>Take your relationships to the next level.</p></article>
    <article class="service-card"><div class="service-icon" role="img" aria-label="Data analytics icon"></div><h3>BI and Data</h3><p>Discover, connect, and trust your data.</p></article>
    <article class="service-card"><div class="sub-brand"><b>Elevra</b><small>By Norvalith</small></div><h3>Building the Right<br>Team of People</h3><p>Hire resources for your transformation journey.</p></article>
  </div>
  <p class="tech-note">Find out how Norvalith can help you put all the pieces together and get them done.</p>
</section>

<div class="wave-band" role="img" aria-label="Soft flowing line wave decoration"></div>

<section class="people">
  <h2>It’s the People</h2>
  <div class="people-copy">
    <p>The world has changed in the past twenty years. The people you need might not all work for one company. Our clients want the best resources, available quickly. That’s why, in addition to our team of experts, we partner with:</p>
    <ul>
      <li>A large network of expert consultants who are the best at what they do,</li>
      <li>Service providers all over the world to provide the resources and value that are right for you, available 24 x 7.</li>
    </ul>
    <p>People are invariably at the center of our customer’s success. Find out how we can add our experts to yours.</p>
  </div>
  <a class="btn">Out Team</a>
  <div class="people-photo" role="img" aria-label="Photo of colleagues meeting around a wooden office table"></div>
</section>

<section class="testimonials">
  <h2>Testimonials</h2>
  <div class="t-item active" style="top:175px"><div class="avatar" role="img" aria-label="Client portrait"></div><div><b>Lorem ipsum dolor sit amet</b><span>Jhon Smith</span></div></div>
  <div class="t-item" style="top:296px"><div class="avatar" role="img" aria-label="Client portrait"></div><div><b>Lorem ipsum dolor sit amet</b><span>Jesika lrems</span></div></div>
  <div class="t-item" style="top:392px"><div class="avatar" role="img" aria-label="Client portrait"></div><div><b>Lorem ipsum dolor sit amet</b><span>Kristen Macksu</span></div></div>
  <div class="t-item" style="top:488px"><div class="avatar" role="img" aria-label="Client portrait"></div><div><b>Lorem ipsum dolor sit amet</b><span>CHangd Lsoes</span></div></div>
  <div class="quote-panel">
    <svg width="62" height="44" viewBox="0 0 62 44" aria-hidden="true"><g fill="#c7ccd6"><path d="M0 44V24C0 10 8 2 22 0v8c-7 2-10 6-10 12h10v24z"/><path d="M34 44V24C34 10 42 2 56 0v8c-7 2-10 6-10 12h10v24z"/></g></svg>
    <p>Lorem ipsum dolor sit amet, consectetur adipiscing elit, sed do eiusmod tempor incididunt ut labore et dolore magna aliqua. Quis ipsum suspendisse ultrices gravida. Risus commodo viverra maecenas accumsan lacus vel facilisis.</p>
    <b>Json Smith</b>
  </div>
</section>

<section class="partners">
  <h2>Technologies</h2>
  <p class="partners-sub">Lorem ipsum dolor sit amet, consectetur adipiscing eli</p>
  <svg class="arrow" style="left:56px" width="26" height="40" viewBox="0 0 26 40" aria-hidden="true"><path d="M20 4 6 20l14 16" fill="none" stroke="#14171f" stroke-width="4"/></svg>
  <div class="partner-row">
    <span class="partner">Corvane</span>
    <span class="partner">Tesserly Suite</span>
    <span class="partner"><i></i>Stratiqa Cloud</span>
    <span class="partner">Halvorn Operate</span>
  </div>
  <svg class="arrow" style="left:1104px" width="26" height="40" viewBox="0 0 26 40" aria-hidden="true"><path d="M6 4l14 16L6 36" fill="none" stroke="#14171f" stroke-width="4"/></svg>
</section>

<section class="cta">
  <p>Lorem ipsum dolor sit amet, consectetur adipiscing elit, sed do eiusmod tempor incididunt ut labore et dolore magna aliqua.</p>
  <a class="btn">Join Now</a>
</section>

<footer class="site-footer">
  <div class="brand"><span class="dot"></span>Norvalith</div>
  <p class="footer-about">Lorem ipsum dolor sit amet, conse ctetur adipiscing elit, sed do eius mod tempor incididunt ut labore et dolore magna aliqua.</p>
  <div class="f-col" style="left:475px"><h4>Menu</h4><a>Home</a><a>Insights</a><a>Services</a><a>Who We are</a><a>Team</a><a>Contact</a></div>
  <div class="f-col" style="left:627px"><h4>Company</h4><a>About us</a><a>Testimonials</a><a>Legal</a></div>
  <div class="f-col" style="left:795px"><h4>Contact</h4>
    <div class="contact-row"><span class="ic"><svg width="14" height="18" viewBox="0 0 14 18"><path d="M7 0a7 7 0 0 0-7 7c0 5 7 11 7 11s7-6 7-11a7 7 0 0 0-7-7zm0 10a3 3 0 1 1 0-6 3 3 0 0 1 0 6z" fill="#fff"/></svg></span><span>418 Larkmoor Plaza Suite 210,<br>Brookfield, MN 55390</span></div>
    <div class="contact-row"><span class="ic"><svg width="16" height="16" viewBox="0 0 16 16"><path d="M3 1l3 3-2 2c1 2 3 4 5 5l2-2 3 3-2 3C6 14 2 10 1 3z" fill="#fff"/></svg></span><span>Phone:<br>(555) 214-0386</span></div>
  </div>
  <div class="footer-rule"></div>
  <p class="copyright">Copyright © 2023 Norvalith. All Rights Reserved.</p>
</footer>

</body>
</html>
```